Create a Capability Summary in PowerPoint

CAPABILITY SUMMARY:
We have been asked to provide a Capability Summary by a client and we need your help creating a compelling document!
Our firm specializes in placing cleared technical talent with innovative government contracting firms nationwide. Our goal is to position ourselves as the "go to" talent acquisition company for small and large IT contracting firms in the Federal IT market.
We want you to have creative control over this template, but would like to it include some variation of the following:
Cover Slide w/ Logo
About Us
The Vantrel Difference
Benefits We Offer
-noting that, unlike many recruiting forms, we offer generous PTO, 100%
vesting 401K, and healthcare benefits for all employees
The Talent We Work With
-showcase the fact that we work in the following technical areas:
Network & Systems Engineer, Software Development, Data Science,
and Information Assurance
Clients We Work With
Data-Driven Recruiting Process
-funnel or graphic showcasing our multi-stage recruiting process of :
Sourcing -> Data Discovery -> Automated Outreach -> Candidate
Qualification -> Technical Interview -> Offer & On-boarding
Contact Us
Target Market(s)
IT companies looking for top engineering talent.

```html
<!DOCTYPE html>
<html lang="en">
<head>
<meta charset="utf-8">
<title>Vantrel – Capability Summary Template</title>
<link href="https://fonts.googleapis.com/css2?family=Roboto:ital,wght@0,300;0,400;0,500;0,700;1,300&family=Roboto+Mono:wght@400&family=Archivo+Black&display=swap" rel="stylesheet">
<style>
  :root{
    --navy:#1f4e7e;
    --red:#b5381f;
    --orange:#d9541e;
    --cyan:#00afd6;
    --ink:#222;
    --grey:#8a8a8a;
    --paper:#fff;
    --canvas:#e8e8e9;
  }
  *{box-sizing:border-box;margin:0;padding:0}
  html,body{width:1200px;height:2201px;overflow:hidden}
  body{background:linear-gradient(#f0f0f0,#dcdcdd 50%,#ececec);position:relative;font-family:"Roboto",sans-serif;color:var(--ink)}
  .slide{position:absolute;width:542px;height:305px;background:var(--paper);overflow:hidden;box-shadow:3px 4px 6px rgba(0,0,0,.35)}
  .col-l{left:30px}.col-r{left:632px}
  .row1{top:485px}.row2{top:829px}.row3{top:1173px}.row4{top:1518px}.row5{top:1862px}
  .abs{position:absolute}
  .brand{font-family:"Roboto",sans-serif;font-weight:700;color:var(--navy);letter-spacing:-.5px;line-height:1}
  .brand-sm{font-size:19px}
  .pager{position:absolute;top:18px;right:18px;display:flex;align-items:center;gap:4px;font-size:7px;color:var(--grey)}
  .title{font-weight:400;letter-spacing:2px;line-height:1.15;color:var(--ink)}
  .mono{font-family:"Roboto Mono",monospace;font-size:7.3px;line-height:1.5;color:#555}
  .photo{position:absolute}

  /* cover */
  .cover{left:30px;top:26px;width:721px;height:405px}
  .cover .photo{inset:0;background:linear-gradient(180deg,#5d6470 0%,#9ea3aa 30%,#e9e6e1 52%,#d9c9a8 70%,#b9893f 85%,#8a6a3a 100%)}
  .cover .brand{position:absolute;left:0;right:0;top:160px;text-align:center;font-size:92px;letter-spacing:2px}
  .cover .tagline{position:absolute;left:0;right:0;top:276px;text-align:center;font-size:13.5px;letter-spacing:5px;color:var(--navy);padding-left:22px}

  .features{position:absolute;left:786px;top:92px;font-family:"Archivo Black",sans-serif;font-size:21px;color:#111;list-style:none}
  .features li{display:flex;align-items:center;height:30px}
  .features .box{width:18px;height:18px;border:2.5px solid #111;margin-right:25px;box-shadow:2px 2px 0 #111}
  .features .sub{padding-left:56px}
  .features .sub::before{content:"";width:8px;height:8px;background:#111;margin-right:38px}

  /* about */
  .about .title{position:absolute;left:305px;top:138px;font-size:25px}
  .about .mono{position:absolute;left:305px;top:172px;width:210px}

  /* difference */
  .difference .photo{left:0;top:0;width:542px;height:217px;background:linear-gradient(160deg,#3a2a22,#7b5a3e 40%,#a8865d 60%,#5b3a2a)}
  .difference .mono{position:absolute;left:32px;top:240px;width:260px;color:#c4c4c4;font-size:7px}
  .difference .heading{position:absolute;right:35px;top:228px;text-align:left}
  .difference .heading .the{font-size:15px;font-weight:700}
  .difference .heading .brand{font-size:30px;margin-left:4px}
  .difference .heading .big{display:block;font-size:33px;font-weight:700;line-height:1;margin-top:2px}

  /* benefits */
  .benefits .title{position:absolute;left:190px;top:32px;width:170px;text-align:center;font-size:23px;letter-spacing:3px}
  .benefit{position:absolute;color:#fff;text-align:center}
  .benefit .cap{position:absolute;left:0;right:0;bottom:12px;font-family:"Roboto Mono",monospace;font-size:10px;letter-spacing:.5px}
  .benefit .cap small{display:block;font-size:8px;line-height:1.5;padding:0 16px;opacity:.85}
  .b1{left:0;top:58px;width:172px;height:247px;background:linear-gradient(180deg,#7f99a4,#9fb1b3 40%,#846f63 80%,#5b4a42)}
  .b2{left:180px;top:103px;width:182px;height:202px;background:linear-gradient(180deg,#9b8f95,#b7a9a6 45%,#7d7a73)}
  .b3{left:370px;top:58px;width:172px;height:247px;background:linear-gradient(180deg,#3f5a63,#6b7f86 45%,#a69a93 75%,#4a5055)}

  /* client grid */
  .client{position:absolute;font-weight:700;color:var(--navy);font-size:13px;white-space:nowrap;display:flex;align-items:center;gap:5px}
  .client .dot{width:14px;height:14px;border-radius:50%;background:var(--navy)}
  .client .sq{width:14px;height:14px;background:var(--red)}

  /* quote */
  .quote .portrait{position:absolute;left:38px;top:80px;width:146px;height:146px;border-radius:50%;background:radial-gradient(circle at 50% 45%,#8c7a70,#3b3230 70%,#1c1a1a)}
  .quote blockquote{position:absolute;left:235px;top:92px;width:260px;font-style:italic;font-weight:300;font-size:19px;line-height:1.3;color:var(--navy)}
  .quote .who{position:absolute;right:45px;top:227px;text-align:right;color:var(--navy);font-size:14px;font-weight:300}
  .quote .who small{display:block;font-size:6.5px;color:#555}

  /* clients-we-work-with */
  .cww .title{position:absolute;left:270px;top:94px;font-size:24px}
  .cww .mono{position:absolute;left:270px;top:163px;width:190px;color:#bbb;font-size:6.5px}
  .cww .brand{position:absolute;right:22px;bottom:15px;font-size:20px}

  /* talent */
  .talent .title{position:absolute;left:26px;top:115px;font-size:21px}
  .talent ul{position:absolute;left:26px;top:188px;width:190px;display:grid;grid-template-columns:100px 90px;row-gap:18px;list-style:none;font-family:"Roboto Mono",monospace;font-size:9px;letter-spacing:1px;line-height:1.35}
  .talent li{padding-left:12px;position:relative}
  .talent li::before{content:"";position:absolute;left:0;top:5px;width:3px;height:3px;background:#333}

  /* process */
  .process .title{position:absolute;left:0;right:0;top:44px;text-align:center;font-size:22px;color:#222}
  .step{position:absolute;width:120px;font-size:10px;line-height:1.25}
  .step b{font-weight:500;color:var(--navy)}
  .step p{font-size:5.5px;line-height:1.35;color:#333;margin-top:2px}
  .step.left{text-align:right;left:30px}
  .step.right{left:394px}

  /* contact */
  .contact .map{position:absolute;inset:0;background:linear-gradient(135deg,#eef0ee,#dfe6df 50%,#e8ecef)}
  .contact .panel{position:absolute;inset:0;background:var(--cyan);clip-path:polygon(213px 0,542px 0,542px 305px,265px 305px)}
  .contact .title{position:absolute;left:260px;width:300px;text-align:center;top:62px;font-size:22px;letter-spacing:4px;color:#fff}
  .contact .brand{position:absolute;left:272px;top:103px;font-size:50px}
  .contact .info{position:absolute;left:288px;top:173px;color:#fff;font-size:9px}
  .contact .info .mono{color:#fff;font-size:7.5px}
  .contact .info .label{margin-top:9px}
  .contact .info a{color:#2048b8;text-decoration:underline}

  /* thanks */
  .thanks{background:#fff}
  .thanks .photo{left:8px;top:8px;right:8px;bottom:8px;background:linear-gradient(180deg,#60656e 0%,#8c9096 35%,#b8b7b3 60%,#a0865c 80%,#6e5530 100%)}
  .thanks .brand{position:absolute;left:0;right:0;top:78px;text-align:center;font-size:52px}
  .thanks .bye{position:absolute;left:0;right:0;top:150px;text-align:center;color:#eee;font-size:22px;letter-spacing:3px;font-weight:300}
  .socials{position:absolute;left:0;right:0;top:186px;display:flex;justify-content:center;gap:40px}
  .socials span{display:flex;flex-direction:column;align-items:center;gap:3px;font-size:5.5px;color:#ddd}
  .socials i{width:22px;height:22px;border-radius:50%;background:rgba(255,255,255,.55)}
</style>
</head>
<body>

<section class="slide cover">
  <div class="photo" role="img" aria-label="Starry night sky over a snowy field with a person holding a lantern"></div>
  <div class="brand">VANTREL</div>
  <div class="tagline">BUSINESS PRESENTATION TEMPLATE</div>
</section>

<ul class="features">
  <li><span class="box"></span>Ratio 16:9</li>
  <li><span class="box"></span>Full HD</li>
  <li><span class="box"></span>Master Slides &nbsp;easy change</li>
  <li><span class="box"></span>Up to 50 slides</li>
  <li class="sub">Text Slides</li>
  <li class="sub">Text +Images</li>
  <li class="sub">Data Slides</li>
  <li class="sub">Tables</li>
  <li class="sub">Infographics</li>
</ul>

<section class="slide about col-l row1">
  <svg class="abs" width="542" height="305" viewBox="0 0 542 305" role="img" aria-label="Diamond collage of office, server and handshake photos">
    <polygon points="0,0 225,0 0,225" fill="#b9b4ad"/>
    <polygon points="100,0 225,0 160,65" fill="#c9c3ba"/>
    <polygon points="225,0 395,0 155,240 70,155" fill="#3f4550"/>
    <polygon points="160,120 255,215 160,305 70,215" fill="#2a3442"/>
    <polygon points="0,185 80,265 40,305 0,305" fill="#6e5a4a"/>
    <polygon points="0,50 75,125 0,200" fill="#d9d6d0"/>
    <polygon points="160,0 225,0 192,32" fill="var(--red)"/>
    <g fill="none" stroke-width="2">
      <polygon points="150,45 190,85 150,125 110,85" stroke="var(--red)"/>
      <polygon points="309,55 333,79 309,103 285,79" stroke="var(--red)"/>
      <polygon points="62,145 85,168 62,191 39,168" stroke="var(--red)"/>
      <polygon points="200,60 220,80 200,100 180,80" stroke="var(--navy)"/>
    </g>
  </svg>
  <div class="pager">12 <svg width="14" height="22" viewBox="0 0 14 22"><path d="M3 2l8 9-8 9" fill="none" stroke="var(--orange)" stroke-width="3"/></svg></div>
  <h2 class="title">ABOUT US</h2>
  <p class="mono">Ut wisi enim ad minim veniam, quis nostrud exerci tation ullamcorper nibh euismod tincidunt ut laoreet dolore magna aliquam erat volutpat. Ut wisi enim ad minim veniam, quis nostrud .</p>
</section>

<section class="slide difference col-r row1">
  <div class="photo" role="img" aria-label="Team working at a wooden table with laptops, notebooks and drinks"></div>
  <p class="mono">Ut wisi enim ad minim veniam, quis nostrud exerci tation ullamcorper nibh euismod tincidunt ut laoreet dolore magna aliquam erat volutpat</p>
  <h2 class="heading"><span class="the">The</span><span class="brand">VANTREL</span><span class="big">Difference</span></h2>
</section>

<section class="slide benefits col-l row2">
  <div class="abs brand brand-sm" style="left:27px;top:16px">VANTREL</div>
  <div class="pager">14 <svg width="14" height="22" viewBox="0 0 14 22"><path d="M3 2l8 9-8 9" fill="none" stroke="var(--orange)" stroke-width="3"/></svg></div>
  <h2 class="title">BENEFITS WE OFFER</h2>
  <div class="benefit b1" role="img" aria-label="Person splashing barefoot in the sea"><div class="cap">Generous PTO<small>Ut wisi enim ad minim veniam, quis nostrud exerci</small></div></div>
  <div class="benefit b2" role="img" aria-label="Dollar bills and a calculator on a desk"><div class="cap">100% Vesting 401K<small>Ut wisi enim ad minim veniam, quis nostrud exerci</small></div></div>
  <div class="benefit b3" role="img" aria-label="Blood pressure being measured on an arm"><div class="cap">Healthcare Benefits<small>Ut wisi enim ad minim veniam, quis nostrud exerci</small></div></div>
</section>

<section class="slide col-r row2">
  <svg class="abs" width="542" height="305" viewBox="0 0 542 305" aria-hidden="true">
    <polygon points="542,60 542,305 470,305 470,230 535,165" fill="var(--red)"/>
    <polygon points="0,60 80,140 0,220" fill="#f3f3f3"/>
    <g fill="none" stroke="var(--navy)" stroke-width="8">
      <line x1="270" y1="40" x2="150" y2="160"/>
      <line x1="270" y1="40" x2="390" y2="160"/>
      <line x1="150" y1="160" x2="270" y2="270"/>
      <line x1="390" y1="160" x2="270" y2="270"/>
    </g>
    <polygon points="270,0 305,35 270,70 235,35" fill="var(--navy)"/>
    <polygon points="270,240 305,270 270,305 235,270" fill="var(--navy)"/>
    <g fill="none" stroke="var(--navy)" stroke-width="2">
      <polygon points="495,63 527,95 495,127 463,95"/>
      <polygon points="70,205 105,240 70,275 35,240"/>
    </g>
  </svg>
  <div class="abs brand brand-sm" style="left:27px;top:16px">VANTREL</div>
  <div class="client" style="left:85px;top:62px"><span class="dot"></span>Keystone Title</div>
  <div class="client" style="left:320px;top:50px"><span class="dot"></span>Northfield Region</div>
  <div class="client" style="left:28px;top:150px"><span class="sq"></span>Startwell Hub</div>
  <div class="client" style="left:205px;top:150px">Galeforce Gear</div>
  <div class="client" style="left:410px;top:150px"><span class="dot"></span>Ledgerway</div>
  <div class="client" style="left:130px;top:228px">Ashby City</div>
  <div class="client" style="left:320px;top:232px"><span class="sq"></span>Harlow University</div>
</section>

<section class="slide quote col-l row3">
  <div class="abs brand brand-sm" style="left:27px;top:16px">VANTREL</div>
  <div class="pager">15 <svg width="14" height="22" viewBox="0 0 14 22"><path d="M3 2l8 9-8 9" fill="none" stroke="var(--orange)" stroke-width="3"/></svg></div>
  <div class="portrait" role="img" aria-label="Portrait of the client giving the testimonial"></div>
  <blockquote>"I believe in Vantrel, because is a company delivering exactly what the customer needs to get the best job done."</blockquote>
  <div class="who">— Alex Morgan<small>client@example.com</small></div>
</section>

<section class="slide cww col-r row3">
  <svg class="abs" width="542" height="305" viewBox="0 0 542 305" role="img" aria-label="Diamond collage of code on screen, padlock on keyboard and devices">
    <polygon points="120,0 210,0 105,105 55,55" fill="#2c3a4c"/>
    <polygon points="0,40 100,140 0,240" fill="#8f949b"/>
    <polygon points="60,130 190,260 130,305 30,210" fill="#c7cbd0"/>
    <polygon points="100,180 150,230 100,280 50,230" fill="#595f68"/>
    <polygon points="0,240 60,305 0,305" fill="#1f2730"/>
    <g fill="none" stroke="var(--navy)" stroke-width="2">
      <polygon points="38,20 60,42 38,64 16,42"/>
      <polygon points="190,110 230,150 190,190 150,150"/>
      <polygon points="160,130 185,155 160,180 135,155"/>
      <polygon points="100,235 125,260 100,285 75,260"/>
    </g>
  </svg>
  <div class="pager">17 <svg width="14" height="22" viewBox="0 0 14 22"><path d="M3 2l8 9-8 9" fill="none" stroke="var(--orange)" stroke-width="3"/></svg></div>
  <h2 class="title">CLIENTS WE<br>WORK WITH</h2>
  <p class="mono">Ut wisi enim ad minim veniam, quis nostrud exerci tation ullamcorper nibh euismod tincidunt ut laoreet dolore magna aliquam erat volutpat. Ut wisi enim. dolore magna aliquam erat volutpat. Ut wisi enim. magna aliquam erat volutpat. Ut wisi enim. magna aliquam erat volutpat. Ut wisi enim.</p>
  <div class="brand">VANTREL</div>
</section>

<section class="slide talent col-l row4">
  <svg class="abs" width="542" height="305" viewBox="0 0 542 305" role="img" aria-label="Diamond collage of server racks, padlock on keyboard and laptop">
    <polygon points="100,0 440,0 290,150" fill="#4a4f58"/>
    <polygon points="440,0 542,0 542,50 475,115" fill="#2e3a4a"/>
    <polygon points="400,60 520,180 400,300 280,180" fill="#3b4554"/>
    <polygon points="350,220 410,280 350,305 300,280" fill="#a9adb3"/>
    <g fill="none" stroke-width="2">
      <polygon points="405,175 440,210 405,245 370,210" stroke="var(--red)"/>
      <polygon points="490,135 510,155 490,175 470,155" stroke="#fff"/>
    </g>
  </svg>
  <div class="abs brand brand-sm" style="left:27px;top:16px">VANTREL</div>
  <div class="pager">18 <svg width="14" height="22" viewBox="0 0 14 22"><path d="M3 2l8 9-8 9" fill="none" stroke="var(--orange)" stroke-width="3"/></svg></div>
  <h2 class="title">THE TALENT WE<br>WORK WITH</h2>
  <ul>
    <li>Network &amp; Systems Engineer</li>
    <li>Software Development</li>
    <li>Data Science</li>
    <li>Information Assurance</li>
  </ul>
</section>

<section class="slide process col-r row4">
  <div class="abs brand brand-sm" style="left:27px;top:16px">VANTREL</div>
  <div class="pager">19 <svg width="14" height="22" viewBox="0 0 14 22"><path d="M3 2l8 9-8 9" fill="none" stroke="var(--orange)" stroke-width="3"/></svg></div>
  <h2 class="title">RECRUITING PROCESS</h2>
  <svg class="abs" width="542" height="305" viewBox="0 0 542 305" aria-hidden="true">
    <g fill="none" stroke-width="22">
      <path d="M246 133 A55 55 0 0 1 296 133" stroke="var(--navy)"/>
      <path d="M301 135.9 A55 55 0 0 1 325.9 179.1" stroke="var(--red)"/>
      <path d="M325.9 184.9 A55 55 0 0 1 301 228.1" stroke="#2aa7c9"/>
      <path d="M296 231 A55 55 0 0 1 246 231" stroke="#3cbfd8"/>
      <path d="M241 228.1 A55 55 0 0 1 216.1 184.9" stroke="#4cc7dc"/>
      <path d="M216.1 179.1 A55 55 0 0 1 241 135.9" stroke="#2f8fc4"/>
    </g>
    <g fill="#fff" font-size="11" font-family="Roboto, sans-serif" text-anchor="middle">
      <text x="271" y="131">01</text><text x="319" y="159">02</text><text x="319" y="214">03</text>
      <text x="271" y="241">04</text><text x="223" y="214">05</text><text x="223" y="159">06</text>
    </g>
  </svg>
  <div class="step left" style="top:95px"><b>06. Offer &amp;<br>On-boarding</b><p>Lorem ipsum dolor sit amet, consectetur adipiscing elit. In in tortor in urna pulvinar blandit.</p></div>
  <div class="step left" style="top:155px"><b>05. Technical<br>Interview</b><p>Lorem ipsum dolor sit amet, consectetur adipiscing elit. In in tortor in urna pulvinar blandit.</p></div>
  <div class="step left" style="top:214px"><b>04. Candidate<br>Qualification</b><p>Lorem ipsum dolor sit amet, consectetur adipiscing elit. In in tortor in urna pulvinar blandit.</p></div>
  <div class="step right" style="top:95px"><b>01. Sourcing</b><p>Lorem ipsum dolor sit amet, consectetur adipiscing elit. In in tortor in urna pulvinar blandit.</p></div>
  <div class="step right" style="top:155px"><b>02. Data Discovery</b><p>Lorem ipsum dolor sit amet, consectetur adipiscing elit. In in tortor in urna pulvinar blandit.</p></div>
  <div class="step right" style="top:210px"><b>03. Automated<br>Outreach</b><p>Lorem ipsum dolor sit amet, consectetur adipiscing elit. In in tortor in urna pulvinar blandit.</p></div>
</section>

<section class="slide contact col-l row5">
  <div class="map" role="img" aria-label="Street map showing the office location"></div>
  <div class="panel"></div>
  <div class="pager" style="color:#fff">20 <svg width="14" height="22" viewBox="0 0 14 22"><path d="M3 2l8 9-8 9" fill="none" stroke="var(--orange)" stroke-width="3"/></svg></div>
  <h2 class="title">GET IN TOUCH</h2>
  <div class="brand">VANTREL</div>
  <div class="info">
    <div>Address</div>
    <div class="mono">47 Alder Grove Ct. NE<br>Fairmont, VA 20190</div>
    <div style="display:flex;gap:22px">
      <div><div class="label">Email</div><a class="mono">info@vantrel-us.com</a></div>
      <div><div class="label">Phone</div><div class="mono" style="font-family:Roboto,sans-serif">555-014-2286</div></div>
    </div>
  </div>
</section>

<section class="slide thanks col-r row5">
  <div class="photo" role="img" aria-label="Dusky sky over a field with a person holding a lantern"></div>
  <div class="brand">VANTREL</div>
  <div class="bye">THANKS FOR WATCHING</div>
  <div class="socials">
    <span><i></i>@loremipsum</span>
    <span><i></i>@loremipsum</span>
    <span><i></i>@loremipsum</span>
  </div>
</section>

</body>
</html>
```